Hydrographic business needs a business card that reaches hunters and off-road enthusiasts

We need a business card for a new hydrographics company catering to customers such as hunters, off-road ATV riders and custom vehicle enthusiasts. A western theme is preferred but professional. Our service should be thought of as upper end graphic design on firearms, off road vehicles, motorcycles, etc... See www.caldorfx.com for ideas on patterns, colors, etc...

Target Market(s)

Hunters, off road enthusiasts, custom car enthusiasts, motorcycle riders...

Industry/Entity Type

Graphic Design

```html
<!DOCTYPE html>
<html lang="en">
<head>
<meta charset="utf-8">
<title>Caldor FX — Business Card</title>
<link href="https://fonts.googleapis.com/css2?family=Cinzel:wght@400;600&family=Open+Sans:wght@400;600;700;800&display=swap" rel="stylesheet">
<style>
  :root {
    --page-bg: #f4f4f4;
    --wood-dark: #4a3322;
    --wood-mid: #7a5a3e;
    --wood-light: #9a7655;
    --frame-silver: #d9d9d9;
    --frame-edge: #6f6f6f;
    --steel-light: #f2f2f2;
    --steel-mid: #c6c6c6;
    --steel-dark: #9c9c9c;
    --ink: #1d1d1d;
    --badge-silver: #e6e6e6;
    --tagline: #e8e2da;
  }
  * { box-sizing: border-box; margin: 0; padding: 0; }
  html, body { width: 1200px; height: 900px; overflow: hidden; }
  body {
    background: var(--page-bg);
    font-family: "Open Sans", Arial, sans-serif;
    position: relative;
  }
  .card {
    position: absolute;
    top: 300px;
    width: 520px;
    height: 300px;
    border-radius: 16px;
    overflow: hidden;
    box-shadow: 0 10px 24px rgba(0,0,0,0.18);
  }
  .card--front { left: 50px; }
  .card--back { left: 630px; }

  /* Front */
  .wood-surface {
    position: absolute; inset: 0;
    background:
      repeating-linear-gradient(90deg, rgba(0,0,0,0.28) 0 2px, transparent 2px 40px),
      linear-gradient(180deg, var(--wood-light), var(--wood-mid) 45%, var(--wood-dark));
  }
  .card-frame {
    position: absolute; inset: 9px;
    border: 4px solid var(--frame-silver);
    border-radius: 12px;
    box-shadow: 0 0 0 1px var(--frame-edge), inset 0 0 0 1px var(--frame-edge);
  }
  .brand-name {
    position: absolute;
    left: 0; right: 0; top: 100px;
    text-align: center;
    font-family: "Open Sans", Arial, sans-serif;
    font-weight: 800;
    font-size: 52px;
    letter-spacing: 3px;
    color: var(--badge-silver);
  }
  .tagline {
    position: absolute;
    left: 20px; right: 20px; bottom: 24px;
    text-align: center;
    font-family: "Cinzel", Georgia, serif;
    font-size: 10.5px;
    letter-spacing: 1.6px;
    color: var(--tagline);
    white-space: nowrap;
  }

  /* Back */
  .steel-surface {
    position: absolute; inset: 0;
    background: linear-gradient(180deg, var(--steel-dark) 0%, var(--steel-light) 30%, var(--steel-mid) 60%, var(--steel-light) 100%);
  }
  .card--back .card-frame {
    border-color: #b9b9b9;
    box-shadow: 0 0 0 1px #555, inset 0 0 0 1px #555;
  }
  .holder-name {
    position: absolute;
    left: 0; right: 0; top: 28px;
    text-align: center;
    font-weight: 700;
    font-size: 21px;
    color: var(--ink);
  }
  .contact-list {
    position: absolute;
    left: 30px; top: 186px;
    list-style: none;
    font-size: 15px;
    line-height: 20px;
    color: var(--ink);
  }
  .contact-list li { display: flex; align-items: flex-start; gap: 7px; }
  .contact-list svg { width: 13px; height: 13px; margin-top: 4px; flex: none; fill: var(--ink); }
  .contact-list .indent { padding-left: 20px; }
  .service-list {
    position: absolute;
    right: 30px; top: 184px;
    list-style: none;
    text-align: right;
    font-weight: 600;
    font-size: 13px;
    color: var(--ink);
  }
  .service-list li { margin-bottom: 14px; }
</style>
</head>
<body>

  <section class="card card--front" aria-label="Card front">
    <div class="wood-surface" role="img" aria-label="Weathered vertical wooden plank background"></div>
    <div class="card-frame"></div>
    <div class="brand-name">CALDOR FX</div>
    <p class="tagline">The best and most reliable hydrographics service in Texas</p>
  </section>

  <section class="card card--back" aria-label="Card back">
    <div class="steel-surface"></div>
    <div class="card-frame"></div>
    <h1 class="holder-name">WADE CALDOR</h1>

    <ul class="contact-list">
      <li>
        <svg viewBox="0 0 16 16" aria-hidden="true"><path d="M3.5 1l3 3-1.6 1.8c.9 2 2.4 3.5 4.3 4.3L11 8.5l3 3-2 2.5C6.5 14 2 9.5 1 3.5z"/></svg>
        <span>214-555-0187</span>
      </li>
      <li>
        <svg viewBox="0 0 16 16" aria-hidden="true"><path d="M8 1L1 7.5h2V15h4v-4h2v4h4V7.5h2z"/></svg>
        <span>112 Mesa Ridge Road</span>
      </li>
      <li class="indent"><span>Cedar Bend, TX 75480</span></li>
      <li>
        <svg viewBox="0 0 16 16" aria-hidden="true"><path d="M8 1a7 7 0 100 14A7 7 0 008 1zm0 1.5c.8 0 1.7 1.4 2 3.5H6c.3-2.1 1.2-3.5 2-3.5zM2.6 7h2.9v2H2.6a5.5 5.5 0 010-2zm3.9 0h3v2h-3zm4 0h2.9a5.5 5.5 0 010 2h-2.9zM6 10h4c-.3 2.1-1.2 3.5-2 3.5S6.3 12.1 6 10z"/></svg>
        <span>www.caldorfx.com</span>
      </li>
      <li>
        <svg viewBox="0 0 16 16" aria-hidden="true"><path d="M1 4h14v9H1zm1.5 1.2L8 9l5.5-3.8V5h-11z"/></svg>
        <span>wade@caldorfx.com</span>
      </li>
    </ul>

    <ul class="service-list">
      <li>Firearm Hydrographics</li>
      <li>ATV Hydrographics</li>
      <li>Hydrographics</li>
    </ul>
  </section>

</body>
</html>
```